Marrowby Electric
Business Cards
Marrowby Electric -
Creative Brief
Modern
Peter Marrowby
Owner
17 Orvell St. Brookfield CT. 06804
pete@marrowbyelectric-example.com
www.marrowbyelectric-example.com
E-1 #374620

```html
<!DOCTYPE html>
<html lang="en">
<head>
<meta charset="utf-8">
<title>Marrowby Electric – Business Cards</title>
<link rel="stylesheet" href="https://fonts.googleapis.com/css2?family=Arimo:wght@400;700&display=swap">
<style>
  :root{
    --bg:#e9eaec;
    --card:#ffffff;
    --navy:#0a2f57;
    --blue:#1b6fb3;
    --sky:#4ea3dc;
    --ink:#2b2b2b;
    --license:#2a78c2;
    --ghost:#e3e8ee;
  }
  *{box-sizing:border-box;margin:0;padding:0}
  html,body{width:1200px;height:852px;overflow:hidden;background:var(--bg);font-family:"Arimo",Arial,sans-serif}
  .stage{position:relative;width:1200px;height:852px}
  .card{position:absolute;width:520px;height:300px;background:var(--card);border-radius:22px;overflow:hidden;box-shadow:0 8px 24px rgba(0,0,0,.18)}
  .card--top{left:70px;top:80px}
  .card--bottom{left:610px;top:470px}
  .card__band{position:absolute;left:0;top:0;width:520px;height:90px}
  .brand{position:absolute;left:26px;display:flex;align-items:center;gap:10px}
  .card--top .brand{top:96px}
  .card--bottom .brand{top:88px}
  .brand__mark{width:30px;height:30px;background:var(--blue);border-radius:5px}
  .brand__name{font-weight:700;font-size:27px;color:var(--navy);letter-spacing:.5px;line-height:1;text-transform:uppercase}
  .ghost-mark{position:absolute;width:96px;height:96px;border-radius:14px;background:var(--ghost);opacity:.8;transform:rotate(-12deg)}
  .card--top .ghost-mark{left:340px;top:110px}
  .card--bottom .ghost-mark{left:360px;top:78px}
  .owner{position:absolute;text-align:center;line-height:1.2}
  .owner__name{font-weight:700;font-size:17px}
  .owner__role{font-size:12px}
  .card--top .owner{left:270px;width:210px;top:16px;color:#fff}
  .card--bottom .owner{left:300px;width:200px;top:172px;color:var(--navy)}
  .card--bottom .owner__role{color:var(--ink)}
  .contact{position:absolute;left:26px;font-size:12.5px;color:var(--ink);line-height:20px;list-style:none}
  .card--top .contact{top:150px}
  .card--bottom .contact{top:142px}
  .contact li{display:flex;align-items:center;gap:6px}
  .contact svg{width:12px;height:12px;flex:none}
  .contact .license{color:var(--license);margin-top:4px}
</style>
</head>
<body>
<main class="stage">

  <section class="card card--top">
    <svg class="card__band" viewBox="0 0 520 90" aria-hidden="true">
      <defs>
        <linearGradient id="bandA" x1="0" x2="1" y1="0" y2="0">
          <stop offset="0" stop-color="#07203f"/>
          <stop offset=".55" stop-color="#0d4f8c"/>
          <stop offset="1" stop-color="#1f7cc4"/>
        </linearGradient>
      </defs>
      <path d="M0 0H520V70C400 68 220 46 0 40Z" fill="url(#bandA)"/>
      <path d="M0 44C220 50 400 72 520 74" stroke="#4ea3dc" stroke-width="2" fill="none" opacity=".6"/>
    </svg>
    <div class="ghost-mark" aria-hidden="true"></div>
    <div class="owner"><div class="owner__name">Peter Marrowby</div><div class="owner__role">Owner</div></div>
    <div class="brand"><span class="brand__mark"></span><span class="brand__name">Marrowby Electric</span></div>
    <ul class="contact">
      <li>17 Orvell St. Brookfield CT. 06804</li>
      <li><svg viewBox="0 0 12 12"><path d="M3 1l2 2-1 1.5c.6 1.3 1.6 2.3 2.9 2.9L8.4 6.4l2 2-1.2 1.9C5 10 2 7 1.7 2.2z" fill="#1b6fb3"/></svg>203-555-0147
        <svg viewBox="0 0 12 12"><rect x="3" y=".5" width="6" height="11" rx="1.2" fill="#1b6fb3"/><rect x="4" y="2" width="4" height="6" fill="#fff"/></svg>203-555-0182</li>
      <li><svg viewBox="0 0 12 12"><circle cx="6" cy="6" r="6" fill="#1b6fb3"/><rect x="2.5" y="3.8" width="7" height="4.6" fill="#fff"/><path d="M2.5 3.8L6 6.6 9.5 3.8" stroke="#1b6fb3" stroke-width=".8" fill="none"/></svg>pete@marrowbyelectric-example.com</li>
      <li><svg viewBox="0 0 12 12"><circle cx="6" cy="6" r="5.5" fill="none" stroke="#1b6fb3" stroke-width="1"/><path d="M.5 6h11M6 .5c-2.5 3-2.5 8 0 11M6 .5c2.5 3 2.5 8 0 11" stroke="#1b6fb3" stroke-width=".8" fill="none"/></svg>www.marrowbyelectric-example.com</li>
      <li class="license">License No : E-1 #374620</li>
    </ul>
  </section>

  <section class="card card--bottom">
    <svg class="card__band" viewBox="0 0 520 90" aria-hidden="true">
      <defs>
        <linearGradient id="bandB" x1="0" x2="1" y1="0" y2="0">
          <stop offset="0" stop-color="#07203f"/>
          <stop offset=".55" stop-color="#0d4f8c"/>
          <stop offset="1" stop-color="#1f7cc4"/>
        </linearGradient>
      </defs>
      <path d="M0 0H520V52C400 50 220 38 0 32Z" fill="url(#bandB)"/>
      <path d="M0 36C220 42 400 54 520 56" stroke="#4ea3dc" stroke-width="2" fill="none" opacity=".6"/>
    </svg>
    <div class="ghost-mark" aria-hidden="true"></div>
    <div class="brand"><span class="brand__mark"></span><span class="brand__name">Marrowby Electric</span></div>
    <div class="owner"><div class="owner__name">Peter Marrowby</div><div class="owner__role">Owner</div></div>
    <ul class="contact">
      <li>17 Orvell St. Brookfield CT. 06804</li>
      <li><svg viewBox="0 0 12 12"><path d="M3 1l2 2-1 1.5c.6 1.3 1.6 2.3 2.9 2.9L8.4 6.4l2 2-1.2 1.9C5 10 2 7 1.7 2.2z" fill="#1b6fb3"/></svg>203-555-0147
        <svg viewBox="0 0 12 12"><rect x="3" y=".5" width="6" height="11" rx="1.2" fill="#1b6fb3"/><rect x="4" y="2" width="4" height="6" fill="#fff"/></svg>203-555-0182</li>
      <li><svg viewBox="0 0 12 12"><circle cx="6" cy="6" r="6" fill="#1b6fb3"/><rect x="2.5" y="3.8" width="7" height="4.6" fill="#fff"/><path d="M2.5 3.8L6 6.6 9.5 3.8" stroke="#1b6fb3" stroke-width=".8" fill="none"/></svg>pete@marrowbyelectric-example.com</li>
      <li><svg viewBox="0 0 12 12"><circle cx="6" cy="6" r="5.5" fill="none" stroke="#1b6fb3" stroke-width="1"/><path d="M.5 6h11M6 .5c-2.5 3-2.5 8 0 11M6 .5c2.5 3 2.5 8 0 11" stroke="#1b6fb3" stroke-width=".8" fill="none"/></svg>www.marrowbyelectric-example.com</li>
      <li class="license">License No : E-1 #374620</li>
    </ul>
  </section>

</main>
</body>
</html>
```